Velvet Dune is a premium Spa and Salon only professional tanning brand.

We need a email template/newsletter that we can send to our client base any time we would like to share information with them.
Whether this is launching our Christmas gift, or sharing up and coming training dates it will be another avenue for us to stay in touch with our clients.
We like to think ourselves as the 'Marchetti handbag' in the tanning world, Velvet Dune is a brand that is desirable and exclusive and has people hooked once they trial the brand and are blown away by the results.
www.velvet-dune.com

```html
<!DOCTYPE html>
<html lang="en">
<head>
<meta charset="utf-8">
<title>Velvet Dune Newsletter</title>
<link rel="stylesheet" href="https://fonts.googleapis.com/css2?family=Raleway:wght@300;400;600;700&family=Open+Sans:wght@400;700&family=Arimo:wght@400&display=swap">
<style>
:root{
  --bg-brown:#a9693f;
  --frame:#dfe4de;
  --cream:#f3eee8;
  --cream-low:#f5f0eb;
  --white:#ffffff;
  --text-brown:#a8643a;
  --deep-brown:#8a5236;
  --grey-text:#6f6a66;
  --nav-grey:#7d7873;
  --rule:#d8d2cc;
  --sand:#dcb08b;
  --copper:#b06d44;
  --rust:#7a2414;
}
*{margin:0;padding:0;box-sizing:border-box}
html,body{width:1200px;height:2717px;overflow:hidden}
body{background:var(--bg-brown);font-family:"Arimo",Arial,sans-serif;position:relative}
.abs{position:absolute}
.preheader{top:26px;left:0;width:1200px;text-align:center;color:#f5e8dc;font-size:18px}
.preheader span{text-decoration:underline}
.frame{left:95px;top:72px;width:1010px;height:2498px;background:var(--frame)}
.header{left:113px;top:90px;width:974px;height:227px;background:var(--cream)}
.brand{left:163px;top:118px;font-family:"Raleway",sans-serif;font-weight:700;font-size:46px;line-height:48px;color:var(--deep-brown);letter-spacing:1px}
.share{left:906px;top:196px;display:flex;align-items:center;gap:10px;font-family:"Arimo",sans-serif;font-size:19px;color:var(--text-brown)}
.share i{display:block;width:18px;height:18px;border-radius:50%}
.share .s1{background:#4a6aa5}.share .s2{background:#4fb0df}
.header-rule{left:163px;top:245px;width:874px;height:2px;background:var(--rule)}
.nav{left:113px;top:266px;width:974px;text-align:center;font-family:"Raleway",sans-serif;font-size:21px;letter-spacing:4px;color:var(--nav-grey);white-space:nowrap}
.nav b{font-weight:400;margin:0 14px}
.hero{left:113px;top:317px;width:974px;height:933px;background:var(--white)}
.hero-title{left:113px;top:382px;width:974px;text-align:center;font-family:"Raleway",sans-serif;font-weight:300;font-size:62px;line-height:74px;color:var(--grey-text);white-space:nowrap}
.hero-lede{left:180px;top:462px;width:840px;text-align:center;font-size:15.5px;line-height:19px;color:var(--grey-text)}
.hero-rule{left:177px;top:537px;width:833px;height:2px;background:var(--rule)}
.product-shot{left:140px;top:640px;width:426px;height:480px;background:linear-gradient(90deg,#eceae6,#fafafa 45%,#e8e4de);border-radius:30px 30px 20px 20px}
.organic-badge{left:412px;top:596px;width:158px;height:158px;border-radius:50%;background:var(--copper)}
.revolution{left:600px;top:632px;width:430px;text-align:center;font-family:"Raleway",sans-serif;font-weight:300;font-size:44px;line-height:61px;color:var(--grey-text);white-space:nowrap}
.hero-copy{left:611px;top:786px;width:408px;font-size:20px;line-height:23.5px;color:var(--text-brown);text-align:justify}
.hero-copy p+p{margin-top:23px}
.btn{left:786px;top:1084px;width:226px;height:62px;background:var(--sand);color:var(--deep-brown);font-family:"Raleway",sans-serif;font-size:26px;display:flex;align-items:center;justify-content:center;gap:12px}
.tri{width:0;height:0;border-left:12px solid currentColor;border-top:8px solid transparent;border-bottom:8px solid transparent}
.range{left:113px;top:1250px;width:974px;height:1320px;background:var(--cream-low)}
.range-title{left:136px;top:1296px;font-family:"Raleway",sans-serif;font-weight:400;font-size:43px;color:var(--deep-brown)}
.card{width:464px;height:254px;color:var(--white);padding:72px 0 0 98px;white-space:nowrap}
.card.gradual{left:129px;top:1383px;background:var(--sand);color:var(--copper)}
.card.original{left:618px;top:1383px;background:var(--copper)}
.card.dark{left:618px;top:1834px;background:var(--rust)}
.bottle{position:absolute;left:24px;top:60px}
.card h3{font-family:"Open Sans",sans-serif;font-weight:700;font-size:41px;line-height:48px}
.card .sub{font-family:"Raleway",sans-serif;font-size:27px;line-height:32px}
.card .more{margin-top:18px;font-family:"Open Sans",sans-serif;font-size:19px;display:flex;align-items:center;gap:10px}
.card.gradual .more{color:var(--deep-brown)}
.desc{font-size:18px;line-height:22px;color:var(--text-brown)}
.desc.d1{left:131px;top:1655px;width:462px}
.desc.d2{left:618px;top:1655px;width:460px}
.desc.d3{left:618px;top:2097px;width:455px}
.model{left:113px;top:1789px;width:498px;height:735px;background:linear-gradient(160deg,#e9b35a 0%,#c9773a 30%,#e8c2a4 55%,#f1e6dc 100%)}
.foot-rule{left:611px;top:2207px;width:471px;height:3px;background:var(--rule)}
.address{left:611px;top:2224px;width:464px;text-align:right;font-size:18px;line-height:29.5px;color:var(--text-brown);font-style:normal}
.badge-square{left:866px;top:2452px;width:74px;height:64px;background:#e5d6c8;border-radius:6px}
.badge-circle{left:985px;top:2447px;width:72px;height:72px;border-radius:50%;background:var(--copper)}
</style>
</head>
<body>
<div class="abs preheader">You're getting this email because you joined us. Not feelin' it? <span>Unsubscribe</span>.</div>
<div class="abs frame"></div>

<div class="abs header"></div>
<div class="abs brand">VELVET<br>DUNE</div>
<div class="abs share">Share <i class="s1"></i><i class="s2"></i></div>
<div class="abs header-rule"></div>
<nav class="abs nav">ABOUT<b>•</b>NEWS<b>•</b>PRODUCTS<b>•</b>TIPS<b>•</b>STOCKISTS</nav>

<section class="abs hero"></section>
<h1 class="abs hero-title">A GIFT WITH EVERY ORDER!</h1>
<p class="abs hero-lede">Lorem ipsum dolor sit amet, consectetur adipisicing elit, sed do eiusmod tempor incididunt ut labore et dolore magna aliqua. Ut enim ad minim veniam, quis nostrud exercitation ullamco laboris nisi ut aliquip ex ea commodo consequat.</p>
<div class="abs hero-rule"></div>
<div class="abs product-shot" role="img" aria-label="Product photo of three white tanning bottles with autumn leaf print"></div>
<div class="abs organic-badge" role="img" aria-label="Organic badge"></div>
<h2 class="abs revolution">A REVOLUTION IN<br>SELF TANNING</h2>
<div class="abs hero-copy">
  <p>Velvet Dune has been developed with a unique organic formula, enriched with deep moisturisers and free from paraben and alcohol, ensuring a streak-free, soft finish.</p>
  <p>This organic formula is enriched with deep moisturisers and exotic botanical extracts that tone and firm the skin fighting cellulite whilst developing a naturally youthful, sunkissed glow.</p>
</div>
<a class="abs btn"><span class="tri"></span>LEARN MORE</a>

<section class="abs range"></section>
<h2 class="abs range-title">OUR PRODUCT RANGE</h2>

<div class="abs card gradual">
  <svg class="bottle" width="46" height="136" viewBox="0 0 46 136"><rect x="14" y="0" width="18" height="22" rx="3" fill="#fff"/><rect x="0" y="26" width="46" height="110" rx="8" fill="#fff"/></svg>
  <h3>GRADUAL TAN</h3><div class="sub">DAILY LOTION</div>
  <div class="more"><span class="tri"></span>LEARN MORE</div>
</div>
<div class="abs card original">
  <svg class="bottle" width="46" height="136" viewBox="0 0 46 136"><rect x="14" y="0" width="18" height="22" rx="3" fill="#fff"/><rect x="0" y="26" width="46" height="110" rx="8" fill="#fff"/></svg>
  <h3>TANNING MIST</h3><div class="sub">ORIGINAL</div>
  <div class="more"><span class="tri"></span>LEARN MORE</div>
</div>
<p class="abs desc d1">Much like our Gradual Tan, our Original and Dark formulas contain an organic formula that comes enriched with the same deep moisturisers and exotic botanicals that help tone and firm the skin, whilst developing a naturally youthful, sun-kissed glow</p>
<p class="abs desc d2">This organic formula is enriched with deep moisturisers and exotic botanical extracts that tone and firm the skin fighting cellulite whilst developing a naturally youthful, sunkissed glow.</p>

<div class="abs model" role="img" aria-label="Photo of a woman seen from behind wrapped in a towel, surrounded by swirling autumn leaves"></div>

<div class="abs card dark">
  <svg class="bottle" width="46" height="136" viewBox="0 0 46 136"><rect x="14" y="0" width="18" height="22" rx="3" fill="#fff"/><rect x="0" y="26" width="46" height="110" rx="8" fill="#fff"/></svg>
  <h3>TANNING MIST</h3><div class="sub">DARK</div>
  <div class="more"><span class="tri"></span>LEARN MORE</div>
</div>
<p class="abs desc d3">For those with darker skin tones or this preference, these additional products provide the option of a richer darker colour.</p>

<div class="abs foot-rule"></div>
<address class="abs address">Velvet Dune<br>hello@velvet-dune.com<br>Larchfield Business Centre<br>Millbrook Road Industrial Estate<br>Ashford Vale, County Down BT40 7QP</address>
<div class="abs badge-square" role="img" aria-label="Cruelty-free badge"></div>
<div class="abs badge-circle" role="img" aria-label="Organic badge"></div>
</body>
</html>
```